Coffee House With Cycling Theme Wants Business Cards

We want to create a business card for a coffee house that has a cycling theme. We expect to use the current logo on one side of the business card and we have been considering adding the words 'COFFEE HOUSE' underneath (see example). For the other side of the business card we want an interesting design with tag-line, address and social media links (the normal business card stuff). See examples provided but we are not fixed on having it exactly as shown, we are very open to great creative ideas. Please note our logo has the initials ‘RM' in orange embedded in the design and this must be retained. However, you can play with the words COFFEE HOUSE as well as use the orange color on the backside of the business card, as you see fit. For an image on the backside of the business card it can be a photo, hand-drawn or whatever but it must visually combine coffee and cycling in some way. The interior of the Coffee House will be reclaimed wood, rustic and have an urban feel to it with cycling artifacts hanging from the walls/ceiling, etc. Finally, it would be beneficial if the business card design elements can be easily used on flyers and other promotional assets. Good luck, we are looking forward to seeing your creative ideas.

Target Market(s)

Coffee lovers and cycling fans

Contact Information for Business Card

See project description.

Colors

Designer to choose colors to be used in the design.

Requirements
Must have
• Must use the current logo provided and combine a coffee and bike theme.
Nice to have
• Orange is used in current logo and could be used as an accent color on the backside of the business card.

```html
<!DOCTYPE html>
<html lang="en">
<head>
<meta charset="utf-8">
<title>RM Coffee House – Business Card</title>
<link href="https://fonts.googleapis.com/css2?family=Questrial&family=Montserrat:wght@700&display=swap" rel="stylesheet">
<style>
  :root {
    --page-bg: #1e1e1e;
    --brand-orange: #f0652b;
    --ink-dark: #3b3b3b;
    --paper-white: #ffffff;
    --coffee-deep: #2a1610;
    --coffee-mid: #5a3422;
    --coffee-light: #9a6a4a;
    --glow: #f4f1ee;
  }
  * { box-sizing: border-box; margin: 0; padding: 0; }
  html, body { width: 1200px; height: 960px; overflow: hidden; }
  body {
    background: var(--page-bg);
    font-family: "Questrial", "Century Gothic", sans-serif;
    display: flex;
    flex-direction: column;
    align-items: center;
    justify-content: center;
    gap: 40px;
  }
  .card {
    width: 760px;
    height: 434px;
    position: relative;
    overflow: hidden;
    box-shadow: 0 10px 30px rgba(0,0,0,.5);
  }

  /* Front */
  .card-front {
    background: var(--brand-orange);
    display: flex;
    align-items: center;
    justify-content: center;
  }
  .brand-mark {
    display: flex;
    align-items: center;
    gap: 18px;
    font-size: 120px;
    letter-spacing: 4px;
    line-height: 1;
  }
  .card-front .brand-mark { color: var(--paper-white); }
  .brand-dot {
    width: 28px; height: 28px;
    border-radius: 50%;
    background: var(--ink-dark);
  }

  /* Back */
  .card-back { color: var(--paper-white); }
  .back-photo {
    position: absolute; inset: 0;
    background:
      radial-gradient(ellipse at 72% 20%, #7a4a2e 0%, transparent 45%),
      radial-gradient(ellipse at 85% 80%, #4a2a1a 0%, transparent 55%),
      linear-gradient(135deg, var(--coffee-light) 0%, var(--coffee-mid) 45%, var(--coffee-deep) 100%);
  }
  .back-glow {
    position: absolute; inset: 0;
    background: linear-gradient(90deg,
      rgba(244,241,238,.0) 0%,
      rgba(244,241,238,.65) 18%,
      var(--glow) 34%,
      rgba(244,241,238,.55) 48%,
      rgba(244,241,238,0) 60%);
  }
  .back-logo {
    position: absolute;
    left: 150px; top: 150px;
  }
  .card-back .brand-mark { color: var(--brand-orange); font-size: 100px; }
  .divider {
    position: absolute;
    left: 430px; top: 50px;
    width: 2px; height: 300px;
    background: var(--paper-white);
  }
  .contact {
    position: absolute;
    left: 455px; top: 58px;
    width: 290px;
  }
  .contact-name {
    font-family: "Montserrat", "Century Gothic", sans-serif;
    font-weight: 700;
    font-size: 26px;
  }
  .contact-title { font-size: 16px; margin-top: 2px; margin-bottom: 18px; opacity: .9; }
  .contact-list { list-style: none; }
  .contact-list li {
    display: flex;
    align-items: flex-start;
    gap: 12px;
    font-size: 17px;
    line-height: 1.3;
    margin-bottom: 12px;
  }
  .contact-list svg { flex: none; width: 18px; height: 18px; margin-top: 2px; fill: var(--paper-white); }
</style>
</head>
<body>

  <section class="card card-front">
    <div class="brand-mark"><span class="brand-dot"></span>RM</div>
  </section>

  <section class="card card-back">
    <div class="back-photo" role="img" aria-label="Photo of ground coffee in a grinder cup, coffee beans and a cup of coffee on a wooden table"></div>
    <div class="back-glow"></div>

    <div class="back-logo">
      <div class="brand-mark"><span class="brand-dot"></span>RM</div>
    </div>

    <div class="divider"></div>

    <div class="contact">
      <p class="contact-name">Your Name</p>
      <p class="contact-title">Your Title</p>
      <ul class="contact-list">
        <li>
          <svg viewBox="0 0 24 24"><path d="M6.6 10.8a15 15 0 0 0 6.6 6.6l2.2-2.2c.3-.3.7-.4 1-.2 1.1.4 2.3.6 3.6.6.6 0 1 .4 1 1V20c0 .6-.4 1-1 1A17 17 0 0 1 3 4c0-.6.4-1 1-1h3.5c.6 0 1 .4 1 1 0 1.3.2 2.5.6 3.6.1.3 0 .7-.2 1z"/></svg>
          <span>123-456-2100</span>
        </li>
        <li>
          <svg viewBox="0 0 24 24"><path d="M2 5h20v14H2zM4 7v.5l8 5 8-5V7l-8 5z"/></svg>
          <span>youremail@mailbox.com</span>
        </li>
        <li>
          <svg viewBox="0 0 24 24"><path d="M12 2a10 10 0 1 0 0 20 10 10 0 0 0 0-20zm0 4a6 6 0 1 1 0 12 6 6 0 0 1 0-12zm0 3a3 3 0 1 0 0 6 3 3 0 0 0 0-6z"/></svg>
          <span>www.yourwebsite.com</span>
        </li>
        <li>
          <svg viewBox="0 0 24 24"><path d="M12 2a7 7 0 0 0-7 7c0 5 7 13 7 13s7-8 7-13a7 7 0 0 0-7-7zm0 9.5a2.5 2.5 0 1 1 0-5 2.5 2.5 0 0 1 0 5z"/></svg>
          <span>Your address, city<br>state, ZIP 0000</span>
        </li>
      </ul>
    </div>
  </section>

</body>
</html>
```